Business Card Design

Consultation for design, construction athletic facilities specializing in synthetic turf systems and all weather running track systems.
Motto "True Owner Representation"
New Company that we'd like to highlight the LOGO first and foremost with the colors of the background and font as primary colors of the card too if possible. I've also attached a typical larger project design layout that could be used in the background to highlight our design and construction specialty.
Website is something we want very noticeable for driving traffic.
Target Market(s)
Athletic Directors, Designers, Government and Military, Contractors
Industry/Entity Type
Construction
Contact Information for Business Card
Peter L. Vandrell CFB, CTB
48317 W 63rd Ave
Harlow Ridge, WA 99482
C +1 503.555.0147
O +1 808.555.0182
Peter@fieldlaneco.example
www.fieldlaneco.example

```html
<!DOCTYPE html>
<html lang="en">
<head>
<meta charset="utf-8">
<title>Corvane Fields – Business Card</title>
<link rel="stylesheet" href="https://fonts.googleapis.com/css2?family=Merriweather:wght@700&family=Open+Sans:wght@300;400&display=swap">
<style>
  :root {
    --page: #e9e6e1;
    --card-dark: #0d0d0d;
    --card-dark-edge: #1f1f1f;
    --gold: #f0a81c;
    --gold-soft: #d9962a;
    --card-light: #fbfbfb;
    --ink-grey: #7a7a7a;
    --plan-light: #f1f1f1;
    --plan-mid: #d4d4d4;
  }
  * { box-sizing: border-box; margin: 0; padding: 0; }
  html, body { width: 1200px; height: 1023px; overflow: hidden; background: var(--page); }
  .canvas { position: relative; width: 1200px; height: 1023px; }

  .card { position: absolute; width: 700px; height: 400px; border-radius: 6px; overflow: hidden; box-shadow: 0 12px 30px rgba(0,0,0,.25); }

  /* Front */
  .card-front { left: 60px; top: 70px; background: linear-gradient(160deg, var(--card-dark-edge) 0%, var(--card-dark) 55%, #000 100%); color: var(--gold); }
  .brand { position: absolute; display: flex; align-items: center; gap: 14px; }
  .card-front .brand { left: 50px; top: 150px; }
  .brand-dot { width: 24px; height: 24px; border-radius: 50%; background: var(--gold); flex: none; }
  .brand-name { font-family: "Open Sans", sans-serif; font-weight: 300; font-size: 30px; line-height: 36px; letter-spacing: 3px; color: var(--gold); }
  .brand-name span { display: block; }
  .holder { position: absolute; left: 300px; top: 60px; font-family: "Merriweather", serif; font-weight: 700; font-size: 24px; color: var(--gold); white-space: nowrap; }
  .holder .creds { font-family: "Open Sans", sans-serif; font-weight: 400; font-size: 15px; margin-left: 6px; }
  .contacts { position: absolute; left: 300px; top: 118px; list-style: none; font-family: "Open Sans", sans-serif; font-size: 17px; line-height: 30px; color: var(--gold); }
  .contacts li { display: flex; align-items: center; gap: 12px; white-space: nowrap; }
  .contacts svg { width: 20px; height: 20px; flex: none; }
  .contacts .web { font-size: 20px; }
  .gold-rule { position: absolute; left: 0; right: 0; top: 286px; height: 2px; background: linear-gradient(90deg, transparent, var(--gold) 30%, var(--gold) 80%, transparent); }
  .address { position: absolute; left: 300px; top: 310px; font-family: "Open Sans", sans-serif; font-size: 16px; color: var(--gold-soft); white-space: nowrap; }

  /* Back */
  .card-back { left: 440px; top: 560px; background: var(--card-light); color: var(--ink-grey); }
  .motto { position: absolute; left: 50px; top: 30px; font-family: "Open Sans", sans-serif; font-size: 15px; letter-spacing: 1.5px; color: var(--ink-grey); }
  .card-back .brand { left: 50px; top: 66px; }
  .card-back .brand-dot { background: var(--ink-grey); width: 22px; height: 22px; }
  .card-back .brand-name { color: var(--ink-grey); font-size: 28px; line-height: 34px; }
  .site-plan { position: absolute; left: 150px; top: 150px; width: 520px; height: 230px; border-radius: 4px; background: radial-gradient(ellipse at 45% 40%, var(--plan-light) 0%, var(--plan-mid) 100%); }
</style>
</head>
<body>
<main class="canvas">
  <section class="card card-front" aria-label="Business card front">
    <div class="brand"><span class="brand-dot"></span><p class="brand-name"><span>Corvane</span><span>Fields</span></p></div>
    <p class="holder">Peter L. Vandrell <span class="creds">| CFB, CTB</span></p>
    <ul class="contacts">
      <li><svg viewBox="0 0 20 20"><rect x="1" y="1" width="18" height="18" rx="3" fill="none" stroke="currentColor"/><rect x="7" y="4" width="6" height="12" rx="1" fill="currentColor"/></svg>+1 503.555.0147</li>
      <li><svg viewBox="0 0 20 20"><rect x="1" y="1" width="18" height="18" rx="3" fill="none" stroke="currentColor"/><path d="M6 5 l3 0 1 3 -2 1 a7 7 0 0 0 3 3 l1 -2 3 1 0 3 a9 9 0 0 1 -9 -9z" fill="currentColor"/></svg>+1 808.555.0182</li>
      <li><svg viewBox="0 0 20 20"><rect x="1" y="1" width="18" height="18" rx="3" fill="none" stroke="currentColor"/><rect x="4" y="6" width="12" height="8" fill="none" stroke="currentColor"/><path d="M4 6 l6 5 6 -5" fill="none" stroke="currentColor"/></svg>Peter@fieldlaneco.example</li>
      <li class="web"><svg viewBox="0 0 20 20"><rect x="1" y="1" width="18" height="18" rx="3" fill="none" stroke="currentColor"/><circle cx="10" cy="10" r="5" fill="none" stroke="currentColor"/><path d="M5 10h10M10 5v10" stroke="currentColor"/></svg>www.fieldlaneco.example</li>
    </ul>
    <div class="gold-rule"></div>
    <p class="address">48317 W 63rd Ave Harlow Ridge, WA 99482</p>
  </section>

  <section class="card card-back" aria-label="Business card back">
    <p class="motto">True Owner Representation</p>
    <div class="brand"><span class="brand-dot"></span><p class="brand-name"><span>Corvane</span><span>Fields</span></p></div>
    <div class="site-plan" role="img" aria-label="Site plan drawing of an athletic complex with running track, field and ball diamonds"></div>
  </section>
</main>
</body>
</html>
```